New Logo, New Business Cards! Looking for Refresh

We're in the process of modernizing our entire organization, and with that came the redesign of our logo (attached). We're looking for a designer to develop our new business cards.
Looking for a design that will bring the company in 2020 and help showcase our new logo. Work with the colors of the logo. Feel free to experiment with the logo in white or black if you want. Both now attached.
Industry/Entity Type
Non Profit
Contact Information for Business Card
Address:
48315 Pelham Crescent, Suite 512
Ashford Vale, ON, K7R 2M5
Name: Dorian Welbeck, MBA
Position: Executive Director
Telephone: 905-371-6248, Ext. 817
Cell Phone: 416-573-2064
Email: dorian@qorvenu.ca
Website: www.qorvenu.ca
Look and feel
Each slider illustrates characteristics of the customer's brand and the style your logo design should communicate.

```html
<!DOCTYPE html>
<html lang="en">
<head>
<meta charset="utf-8">
<title>Qorvenu Business Card</title>
<link href="https://fonts.googleapis.com/css2?family=Lato:wght@400;700;900&display=swap" rel="stylesheet">
<style>
  :root {
    --backdrop: #9b9b9b;
    --forest: #0b3f25;
    --forest-deep: #052d18;
    --leaf: #4f9a44;
    --brand-green: #2f8a3e;
    --front-mark: #1f7a3b;
    --paper: #e2e2e2;
    --paper-light: #ececec;
    --ink: #0c3d22;
    --ink-soft: #4a4a4a;
    --white: #ffffff;
  }
  * { box-sizing: border-box; margin: 0; padding: 0; }
  html, body { width: 1200px; height: 900px; overflow: hidden; }
  body {
    background: var(--backdrop);
    font-family: "Lato", sans-serif;
    position: relative;
  }
  .card {
    position: absolute;
    left: 363px;
    width: 474px;
    height: 270px;
    border-radius: 24px;
    overflow: hidden;
  }
  .card-front {
    top: 145px;
    background: var(--forest);
    display: flex;
    align-items: center;
    justify-content: center;
    padding-bottom: 40px;
  }
  .front-wordmark {
    font-weight: 900;
    font-size: 52px;
    color: var(--front-mark);
    letter-spacing: 1px;
  }
  .card-back {
    top: 484px;
    background: linear-gradient(180deg, var(--paper-light), var(--paper));
  }
  .holder-name {
    position: absolute;
    left: 31px;
    top: 49px;
    font-size: 14.5px;
    font-weight: 700;
    color: var(--ink);
  }
  .holder-title {
    position: absolute;
    left: 31px;
    top: 69px;
    font-size: 11.5px;
    color: var(--ink-soft);
  }
  .contact-list {
    position: absolute;
    left: 31px;
    top: 119px;
    list-style: none;
  }
  .contact-list li {
    display: flex;
    align-items: center;
    height: 15.2px;
    font-size: 11.3px;
    color: var(--ink-soft);
  }
  .contact-list svg {
    width: 10px;
    height: 10px;
    margin-right: 6px;
    fill: var(--brand-green);
  }
  .ext { color: var(--brand-green); }
  .back-wordmark {
    position: absolute;
    left: 268px;
    top: 52px;
    width: 173px;
    text-align: center;
    font-weight: 900;
    font-size: 40px;
    color: var(--brand-green);
  }
  .wave {
    position: absolute;
    left: 0;
    top: 0;
    width: 474px;
    height: 270px;
  }
  .address {
    position: absolute;
    left: 268px;
    top: 227px;
    font-size: 11.3px;
    line-height: 15.3px;
    font-style: normal;
    color: var(--white);
  }
</style>
</head>
<body>
  <section class="card card-front">
    <div class="front-wordmark">Qorvenu</div>
  </section>

  <section class="card card-back">
    <svg class="wave" viewBox="0 0 474 270" aria-hidden="true">
      <path fill="var(--forest)" d="M0,196 C80,226 150,232 230,218 C310,202 380,180 474,192 L474,270 L0,270 Z"/>
      <path fill="var(--leaf)" d="M0,206 C80,236 160,238 240,220 C320,200 390,178 474,186 L474,200 C390,190 320,212 240,232 C160,250 80,248 0,230 Z"/>
      <path fill="var(--forest-deep)" d="M474,200 C390,190 320,212 240,232 C330,216 410,212 474,250 Z"/>
    </svg>

    <h1 class="holder-name">Dorian Welbeck, MBA</h1>
    <p class="holder-title">Executive Director</p>

    <ul class="contact-list">
      <li><svg viewBox="0 0 10 10"><path d="M2.5,0h5a1,1 0 0 1 1,1v8a1,1 0 0 1-1,1h-5a1,1 0 0 1-1-1v-8a1,1 0 0 1 1-1zM3,1.3v6.4h4v-6.4z"/></svg>416-573-2064</li>
      <li><svg viewBox="0 0 10 10"><path d="M2,0.5l1.8,2-0.9,1.2c0.6,1.3 1.6,2.3 2.9,2.9l1.2-0.9 2,1.8-1.2,1.8c-4.3-0.3-7.5-3.5-7.8-7.8z"/></svg>905-371-6248,<span class="ext">&nbsp;Ext.</span>&nbsp;817</li>
      <li><svg viewBox="0 0 10 10"><path d="M0,2h10v6h-10zM0.8,2.6l4.2,3 4.2-3v-0.2h-8.4z"/></svg>dorian@qorvenu.ca</li>
      <li><svg viewBox="0 0 10 10"><circle cx="5" cy="5" r="4.6"/><path d="M0.5,5h9M5,0.5c-2.4,2.5-2.4,6.5 0,9M5,0.5c2.4,2.5 2.4,6.5 0,9" stroke="#e4e4e4" stroke-width="0.6" fill="none"/></svg>www.qorvenu.ca</li>
    </ul>

    <div class="back-wordmark">Qorvenu</div>

    <address class="address">
      48315 Pelham Crescent, Suite 512<br>
      Ashford Vale, ON, K7R 2M5
    </address>
  </section>
</body>
</html>
```